Post Card (5x7) - Pre-foreclosure Image - Harbor Path Partners

(Two-Sided Post Card)
FACING FORECLOSURE? YOU STILL HAVE OPTIONS.
If you’re behind on payments or at risk of foreclosure, you’re not alone—and it’s not too late to take action.
We help homeowners:
• Explore options to stay in their home
• Stop or delay foreclosure
• Sell quickly for a fair price if needed
No pressure. No obligation. Just real solutions tailored to your situation.
Call - (240) 558-2094
Email - marcus@hpbllc-mail.com
Harbor Path Partners LLC
7200 Bramwick Lane, Ellicott City, MD 21043
**Marcus Fennimore is a Licensed Realtor with Copperleaf Homes Realty in Bethesda, Maryland.
(Leave room for mailing address, return address & postage)
Target Market(s)
Distressed Homeowners
Industry/Entity Type
Real Estate

```html
<!DOCTYPE html>
<html lang="en">
<head>
<meta charset="utf-8">
<title>Harbor Path Partners – Postcard</title>
<link href="https://fonts.googleapis.com/css2?family=Mulish:wght@300;400;600;700;800&display=swap" rel="stylesheet">
<style>
:root{
  --page:#dcdadb;
  --ink-dark:#0b0b0b;
  --ink-panel:#2a2a2a;
  --white:#ffffff;
  --soft-white:#e6e6e6;
  --card-light:#f2f1f2;
  --text-dark:#1c1c1c;
  --text-mid:#555555;
  --rule-dark:#555555;
  --rule-mid:#888888;
  --rule-light:#b5b5b5;
  --glow:#f0a43a;
}
*{margin:0;padding:0;box-sizing:border-box}
html,body{width:844px;height:1200px;overflow:hidden;background:var(--page);font-family:"Mulish",sans-serif}
.card{position:absolute;left:64px;width:716px;height:511px;overflow:hidden;box-shadow:0 14px 24px rgba(0,0,0,.25)}
.card--front{top:64px;background:linear-gradient(135deg,#050505 0%,#111 55%,#2b2b2b 100%)}
.card--back{top:625px;background:var(--card-light)}
.abs{position:absolute}
.frame{position:absolute;inset:0}
.skyline-photo{left:0;top:200px;width:470px;height:311px;
  background:
    radial-gradient(ellipse 90px 70px at 232px 140px,rgba(255,210,120,.95),rgba(240,164,58,.6) 40%,transparent 100%),
    radial-gradient(ellipse 260px 160px at 232px 170px,rgba(150,90,30,.7),transparent 80%),
    linear-gradient(180deg,#0b0b0b 0%,#2a1d12 45%,#140e08 70%,#3a2a16 82%,#120c07 100%);
  -webkit-mask-image:linear-gradient(90deg,#000 70%,transparent 100%),linear-gradient(180deg,transparent 0%,#000 25%);
  mask-image:linear-gradient(180deg,transparent 0%,#000 25%);}
.headline{left:50px;color:var(--white);line-height:1}
.headline__light{top:58px;font-size:38px;font-weight:400;letter-spacing:-1px}
.headline__bold{top:103px;font-size:46px;font-weight:800;letter-spacing:-1.5px}
.dashes{display:flex;gap:5px}
.dashes span{height:3px;display:block}
.dashes--front{left:52px;top:159px}
.dashes--front span:nth-child(1){width:87px;background:#555}
.dashes--front span:nth-child(2){width:26px;background:#777}
.dashes--front span:nth-child(3){width:13px;background:#aaa}
.subhead{left:52px;top:175px;color:var(--white);font-size:25px;font-weight:400;letter-spacing:-.8px}
.brand{left:440px;top:62px;width:218px;text-align:center;color:var(--white)}
.brand__mark{width:26px;height:26px;border:2px solid var(--white);margin:0 auto 14px}
.brand__name{font-size:19px;font-weight:700;letter-spacing:3px;white-space:nowrap}
.brand__sub{display:flex;align-items:center;gap:8px;font-size:9px;font-weight:700;letter-spacing:3px;margin-top:3px}
.brand__sub::before,.brand__sub::after{content:"";flex:1;height:1.5px;background:var(--white)}
.note{left:389px;top:227px;width:261px;height:88px;background:var(--ink-panel);color:var(--soft-white);
  padding:14px 18px;font-size:14px;font-weight:300;line-height:19.5px;letter-spacing:-.3px}
.promise{left:389px;top:332px;color:var(--white)}
.promise__lead{font-size:17px;font-weight:700;letter-spacing:-.5px}
.promise__body{font-size:15.5px;font-weight:300;line-height:18.5px;letter-spacing:-.3px;margin-top:3px}
.dashes--promise{left:389px;top:404px}
.dashes--promise span:nth-child(1){width:75px;background:#555}
.dashes--promise span:nth-child(2){width:22px;background:#777}
.dashes--promise span:nth-child(3){width:11px;background:#aaa}
.back-photo{inset:0;background:linear-gradient(180deg,transparent 40%,rgba(200,195,190,.35) 70%,rgba(215,210,205,.4) 100%)}
.services{left:54px;top:44px;color:var(--text-dark)}
.services__title{font-size:27px;font-weight:700;letter-spacing:-1px}
.dashes--back{margin-top:8px}
.dashes--back span:nth-child(1){width:117px;background:var(--rule-dark)}
.dashes--back span:nth-child(2){width:35px;background:var(--rule-mid)}
.dashes--back span:nth-child(3){width:17px;background:var(--rule-light)}
.services__list{list-style:none;margin-top:13px;font-size:18px;font-weight:400;letter-spacing:-.6px;line-height:24px}
.services__list li{display:flex;align-items:center;gap:6px}
.services__list svg{width:13px;height:13px;flex:none}
.contact{left:54px;top:206px;color:var(--text-dark)}
.contact__row{display:flex;align-items:center}
.contact__icon{width:28px;flex:none;display:flex;justify-content:flex-start}
.contact__phone{font-size:34px;font-weight:700;letter-spacing:-1.8px}
.contact__email{font-size:22px;font-weight:400;letter-spacing:-.7px;margin-top:2px}
.contact__address{align-items:flex-start;font-size:18px;font-weight:400;letter-spacing:-.6px;line-height:27px;margin-top:4px}
.bio{left:422px;top:46px;width:290px;font-size:18px;font-weight:400;line-height:26px;letter-spacing:-.6px;color:var(--text-dark)}
.bio strong{font-weight:600;color:var(--text-mid)}
.mail-area{left:422px;top:171px;width:250px;height:266px;border:1px dashed #8a8a8a;background:rgba(245,245,246,.7)}
</style>
</head>
<body>

<section class="card card--front">
  <div class="abs skyline-photo" role="img" aria-label="City skyline silhouetted against a sunset over a river"></div>
  <svg class="frame" width="716" height="511" viewBox="0 0 716 511" aria-hidden="true">
    <polyline points="250,22 694,22 694,345 360,511" fill="none" stroke="#8a8a8a" stroke-width="0.8"/>
  </svg>
  <h1>
    <span class="abs headline headline__light">FACING</span>
    <span class="abs headline headline__bold">FORECLOSURE?</span>
  </h1>
  <div class="abs dashes dashes--front"><span></span><span></span><span></span></div>
  <p class="abs subhead">You Still Have Options.</p>
  <div class="abs brand">
    <div class="brand__mark"></div>
    <div class="brand__name">HARBOR PATH</div>
    <div class="brand__sub">PARTNERS LLC</div>
  </div>
  <p class="abs note">If you’re behind on payments or at risk of foreclosure, you’re not alone and it’s not too late to take action.</p>
  <div class="abs promise">
    <p class="promise__lead">No pressure. No obligation.</p>
    <p class="promise__body">Just real solutions tailored<br>to your situation.</p>
  </div>
  <div class="abs dashes dashes--promise"><span></span><span></span><span></span></div>
</section>

<section class="card card--back">
  <div class="abs back-photo" role="img" aria-label="Faded city skyline along the waterfront"></div>
  <svg class="frame" width="716" height="511" viewBox="0 0 716 511" aria-hidden="true">
    <polyline points="694,21 22,21 22,357 326,511" fill="none" stroke="#222" stroke-width="0.8"/>
    <line x1="399" y1="511" x2="716" y2="345" stroke="#666" stroke-width="0.8"/>
  </svg>
  <div class="abs services">
    <h2 class="services__title">We Help Homeowners</h2>
    <div class="dashes dashes--back"><span></span><span></span><span></span></div>
    <ul class="services__list">
      <li><svg viewBox="0 0 12 12"><path d="M1 6.5 4.2 9.5 11 2" fill="none" stroke="#444" stroke-width="1.4"/></svg>Explore options to stay in their home</li>
      <li><svg viewBox="0 0 12 12"><path d="M1 6.5 4.2 9.5 11 2" fill="none" stroke="#444" stroke-width="1.4"/></svg>Stop or delay foreclosure</li>
      <li><svg viewBox="0 0 12 12"><path d="M1 6.5 4.2 9.5 11 2" fill="none" stroke="#444" stroke-width="1.4"/></svg>Sell quickly for a fair price if needed</li>
    </ul>
  </div>
  <div class="abs contact">
    <div class="contact__row contact__phone">
      <span class="contact__icon"><svg width="20" height="22" viewBox="0 0 24 24"><path d="M6.6 2.5 9.4 7c.3.6.2 1.3-.3 1.7L7.6 10c1.2 2.6 3.6 5 6.3 6.3l1.3-1.5c.4-.5 1.1-.6 1.7-.3l4.5 2.8c.6.4.8 1.1.5 1.7l-1.2 2.4c-.4.7-1.2 1.1-2 .9C10.6 20.4 3.6 13.4 1.7 5.3c-.2-.8.2-1.6.9-2l2.4-1.2c.6-.3 1.3-.1 1.6.4z" fill="#555"/></svg></span>
      240 558 2094
    </div>
    <div class="contact__row contact__email">
      <span class="contact__icon"><svg width="17" height="12" viewBox="0 0 17 12"><rect width="17" height="12" rx="1" fill="#666"/><path d="M0.5 1 8.5 7 16.5 1" fill="none" stroke="#f2f1f2" stroke-width="1.3"/></svg></span>
      marcus@hpbllc-mail.com
    </div>
    <div class="contact__row contact__address">
      <span class="contact__icon" style="padding-top:5px;padding-left:2px"><svg width="12" height="17" viewBox="0 0 12 17"><path d="M6 0C2.7 0 0 2.6 0 5.9 0 10.3 6 17 6 17s6-6.7 6-11.1C12 2.6 9.3 0 6 0zm0 8.2a2.3 2.3 0 1 1 0-4.6 2.3 2.3 0 0 1 0 4.6z" fill="#777"/></svg></span>
      <address style="font-style:normal">Harbor Path Partners LLC<br>7200 Bramwick Lane, Ellicott City,<br>MD 21043</address>
    </div>
  </div>
  <p class="abs bio"><strong>Marcus Fennimore</strong> is a Licensed Realtor with Copperleaf Homes Realty in Bethesda, Maryland.</p>
  <div class="abs mail-area" aria-label="Space for mailing address, return address and postage"></div>
</section>

</body>
</html>
```